Building company buisness cards

We are looking for a sharp modern new look for our business cards.We are a New Zealand based company that specialises in house and land packages.We have attached a photo of the current logo and would like to see if it can be improved somehow if needed.We are open to any colours but we have chosen Black and White at this stage. Feel free to change the font and make the logo smarter looking.Play with the colours and see what looks best.We want a card that looks so good know one will want to throw it away!

Target Market(s)

Building profesonals, home buyers

Industry/Entity Type

Building

Contact Information for Business Card

Derek Haskins
0274930268
derekh@stonerange.co.nz

Font styles to use
Serif
Sans Serif

Colors

Designer to choose colors to be used in the design.

Requirements
Must have
• Just the logo on one side and details on the other
• Clean simple looking card
Nice to have
• Round corners and detail like raised or spot UV
• Something that stands out
Should not have
• To title needed, Director etc

```html
<!DOCTYPE html>
<html lang="en">
<head>
<meta charset="utf-8">
<title>Stonerange Business Cards</title>
<link rel="stylesheet" href="https://fonts.googleapis.com/css2?family=Josefin+Sans:wght@300;700&display=swap">
<style>
  :root {
    --backdrop: #1c1c1d;
    --card: #0b0b0f;
    --ink: #ffffff;
    --ink-soft: #d8d8dc;
  }
  * { margin: 0; padding: 0; box-sizing: border-box; }
  html, body {
    width: 1200px;
    height: 1200px;
    overflow: hidden;
    background: var(--backdrop);
  }
  .canvas {
    position: relative;
    width: 1200px;
    height: 1200px;
  }
  .card {
    position: absolute;
    width: 815px;
    height: 511px;
    background: var(--card);
    box-shadow: 0 10px 40px rgba(0,0,0,0.45);
    overflow: hidden;
  }
  .card--front { left: 147px; top: 56px; }
  .card--back  { left: 238px; top: 631px; }
  .card__lines {
    position: absolute;
    inset: 0;
    width: 100%;
    height: 100%;
  }
  .tagline {
    position: absolute;
    left: 52px;
    top: 46px;
    font-family: "Josefin Sans", sans-serif;
    font-weight: 300;
    font-size: 18px;
    letter-spacing: 0.3px;
    color: var(--ink-soft);
  }
  .details {
    position: absolute;
    left: 140px;
    top: 173px;
    height: 181px;
    padding-left: 27px;
    border-left: 3px solid var(--ink);
    font-family: "Josefin Sans", sans-serif;
    font-weight: 700;
    color: var(--ink);
    text-transform: uppercase;
  }
  .details__name {
    font-size: 35px;
    line-height: 1;
    margin-top: 2px;
  }
  .details__contact {
    margin-top: 50px;
    font-size: 21px;
    line-height: 24px;
  }
  .brand {
    position: absolute;
    right: 42px;
    bottom: 40px;
    display: flex;
    align-items: center;
    gap: 8px;
    font-family: "Josefin Sans", sans-serif;
    font-weight: 700;
    font-size: 30px;
    color: var(--ink);
  }
  .brand__dot {
    width: 34px;
    height: 34px;
    border: 2px solid var(--ink);
    border-radius: 50%;
  }
  .emblem {
    position: absolute;
    left: 317px;
    top: 157px;
    width: 184px;
    height: 184px;
    border: 5px solid var(--ink);
    border-radius: 50%;
    display: flex;
    align-items: center;
    justify-content: center;
    font-family: "Josefin Sans", sans-serif;
    font-weight: 700;
    font-size: 24px;
    color: var(--ink);
  }
</style>
</head>
<body>
<main class="canvas">
  <section class="card card--front" aria-label="Card front">
    <svg class="card__lines" viewBox="0 0 815 511" aria-hidden="true">
      <line x1="484" y1="1" x2="385" y2="139" stroke="#fff" stroke-width="5"/>
      <line x1="226" y1="369" x2="125" y2="513" stroke="#fff" stroke-width="5"/>
    </svg>
    <p class="tagline">Homes inspired by you.</p>
    <div class="details">
      <h1 class="details__name">Derek Haskins</h1>
      <p class="details__contact">0274930268<br>derekh@stonerange.co.nz</p>
    </div>
    <div class="brand">Stonerange<span class="brand__dot"></span></div>
  </section>

  <section class="card card--back" aria-label="Card back">
    <svg class="card__lines" viewBox="0 0 815 511" aria-hidden="true">
      <line x1="586" y1="-2" x2="486" y2="140" stroke="#fff" stroke-width="5"/>
      <line x1="327" y1="369" x2="226" y2="513" stroke="#fff" stroke-width="5"/>
    </svg>
    <div class="emblem">Stonerange</div>
  </section>
</main>
</body>
</html>
```